lawn sign

Lawn Sign
Roofing Gutters Windows

Target Market(s)

roofing

Font styles to use
Sans Serif

Colors
86cfc6
33a6d7
fbee3f
faa54b

Requirements
Must have
• my logo
Nice to have
• designer for now

```html
<!DOCTYPE html>
<html lang="en">
<head>
<meta charset="utf-8">
<title>Lavalle Home Exteriors – Lawn Sign</title>
<link href="https://fonts.googleapis.com/css2?family=PT+Serif:wght@400&display=swap" rel="stylesheet">
<style>
  :root {
    --page: #ffffff;
    --band: #13934a;
    --gold-light: #f2ea45;
    --gold-mid: #e6c936;
    --gold-deep: #dca42f;
    --label-blue: #1d6fc6;
    --mark: #33a6d7;
  }
  * { margin: 0; padding: 0; box-sizing: border-box; }
  html, body { width: 1200px; height: 1200px; overflow: hidden; background: var(--page); }
  .canvas { position: relative; width: 1200px; height: 1200px; }
  .sign {
    position: absolute; left: 34px; top: 222px; width: 1132px; height: 756px;
    background: linear-gradient(90deg, var(--gold-light) 0%, var(--gold-mid) 50%, var(--gold-deep) 100%);
  }
  .sign-band { position: absolute; left: 0; width: 100%; height: 19px; background: var(--band); }
  .sign-band--top { top: 0; }
  .sign-band--bottom { bottom: 0; }
  .brand {
    position: absolute; left: 0; top: 110px; width: 100%;
    display: flex; align-items: center; justify-content: center; gap: 32px;
  }
  .brand__mark { width: 140px; height: 140px; border-radius: 50%; background: var(--mark); flex: none; }
  .brand__name {
    font-family: "PT Serif", serif; font-weight: 400; font-size: 48px;
    color: var(--label-blue); line-height: 1; white-space: nowrap;
  }
  .service { position: absolute; top: 398px; width: 260px; text-align: center; }
  .service--roofing { left: 59px; }
  .service--gutters { left: 436px; }
  .service--windows { left: 813px; }
  .service__icon { display: block; width: 220px; height: 220px; margin: 0 auto; }
  .service__label {
    display: block; margin-top: 40px;
    font-family: "PT Serif", serif; font-size: 37px; letter-spacing: -1px;
    color: var(--label-blue); line-height: 1;
  }
</style>
</head>
<body>
<main class="canvas">
  <section class="sign">
    <div class="sign-band sign-band--top"></div>

    <div class="brand">
      <div class="brand__mark"></div>
      <h1 class="brand__name">Lavalle Home Exteriors Co.</h1>
    </div>

    <div class="service service--roofing">
      <svg class="service__icon" viewBox="-138 -138 276 276" aria-hidden="true">
        <circle r="138" fill="var(--band)"/>
        <rect x="43" y="-52" width="24" height="40" fill="var(--gold-light)"/>
        <polyline points="-99,43 0,-42 99,43" fill="none" stroke="var(--gold-light)" stroke-width="24" stroke-linejoin="miter"/>
      </svg>
      <span class="service__label">ROOFING</span>
    </div>

    <div class="service service--gutters">
      <svg class="service__icon" viewBox="-138 -138 276 276" aria-hidden="true">
        <circle r="138" fill="var(--band)"/>
        <path d="M-86,-70 H30 V-19 H-70 Q-82,-40 -86,-70 Z" fill="var(--gold-light)"/>
        <path d="M30,-70 H86 Q86,-19 58,-19 Q30,-19 30,-70 Z" fill="var(--gold-light)"/>
        <path d="M36,-70 Q38,-30 58,-24 Q80,-30 80,-70" fill="none" stroke="var(--band)" stroke-width="5"/>
        <path d="M6,-10 H46 V25 Q46,52 20,52 H10 V70 H-27 V40 Q-27,16 0,16 H10 V-2 H6 Z" fill="var(--gold-light)"/>
      </svg>
      <span class="service__label">GUTTERS</span>
    </div>

    <div class="service service--windows">
      <svg class="service__icon" viewBox="-138 -138 276 276" aria-hidden="true">
        <circle r="138" fill="var(--band)"/>
        <rect x="-69" y="-70" width="65" height="66" fill="var(--gold-light)"/>
        <rect x="4" y="-70" width="66" height="66" fill="var(--gold-light)"/>
        <rect x="-69" y="4" width="65" height="66" fill="var(--gold-light)"/>
        <rect x="4" y="4" width="66" height="66" fill="var(--gold-light)"/>
      </svg>
      <span class="service__label">WINDOWS</span>
    </div>

    <div class="sign-band sign-band--bottom"></div>
  </section>
</main>
</body>
</html>
```